Dalworth Pitching Mechanics

Private pitching sessions with a Division 1 PJTB baseball pitcher. Would also like a page setup where clients can request sesseions and pay for sessions.

```html
<!DOCTYPE html>
<html lang="en">
<head>
<meta charset="utf-8">
<title>Dalworth Pitching Mechanics</title>
<link href="https://fonts.googleapis.com/css2?family=Poppins:ital,wght@0,400;0,500;0,600;0,700;0,800;1,600;1,700;1,800&display=swap" rel="stylesheet">
<style>
:root{
  --red:#e8191f;
  --black:#050505;
  --ink:#222;
  --text:#333;
  --white:#fff;
  --field:#9a9a9a;
  --hero-a:#2e3a2a;
  --hero-b:#6b6f66;
  --dirt-a:#2a1c14;
  --dirt-b:#4a3424;
}
*{margin:0;padding:0;box-sizing:border-box}
html,body{width:1200px;height:3636px;overflow:hidden}
body{position:relative;background:var(--white);font-family:'Poppins',sans-serif;color:var(--text)}
.abs{position:absolute}
.shapes{position:absolute;left:0;top:0;width:1200px;height:3636px}
.photo{position:absolute}

/* header */
.logo{left:78px;top:30px;display:flex;align-items:center;gap:10px}
.logo-mark{width:22px;height:22px;background:var(--red)}
.logo-name{font-weight:800;font-size:17px;line-height:20px;color:var(--red);letter-spacing:.3px;text-transform:uppercase;width:170px}
.main-nav{right:73px;top:44px;display:flex;gap:27px}
.main-nav a{font-size:13px;font-weight:700;font-style:italic;color:var(--ink);text-decoration:none;text-transform:uppercase}
.main-nav a.active{color:var(--red);text-decoration:underline;text-underline-offset:5px}

/* hero */
.hero-title{left:75px;top:282px;font-size:53px;line-height:54px;font-weight:800;font-style:italic;color:var(--white);text-transform:uppercase}
.hl{color:var(--red)}
.hero-sub{left:75px;top:400px;font-size:21px;line-height:30px;font-weight:600;color:var(--white);width:560px}
.btn{position:absolute;background:var(--red);color:var(--white);font-weight:700;font-size:14px;text-transform:uppercase;display:flex;align-items:center;justify-content:center;text-decoration:none}
.dots{position:absolute;display:flex;gap:10px}
.dots span{width:10px;height:10px;background:var(--white)}
.dots span.on{background:var(--red)}
.dots.grey span{background:#777}
.dots.grey span.on{background:var(--red)}

/* headings */
.section-title{font-weight:700;font-size:31px;line-height:38px;text-transform:uppercase;color:var(--ink)}
.body-copy{font-size:13.5px;line-height:24px;color:var(--text)}

.sessions-title{left:0;width:1200px;top:1404px;text-align:center;color:var(--white);font-size:30px;line-height:40px;font-weight:700;text-transform:uppercase}
.sessions-copy{left:160px;width:880px;top:1496px;text-align:center;color:var(--white);font-size:13.5px;line-height:24px}

/* testimonials */
.testi-card{position:absolute;top:2509px;width:329px;height:196px;background:var(--white);border-left:9px solid #666;padding:12px 16px 0 10px}
.quote{font-size:40px;line-height:30px;font-weight:800;color:var(--red);opacity:.55;height:14px;display:block}
.testi-card p{font-size:13.5px;line-height:24px;color:var(--text);position:relative}
.testi-name{margin-top:6px;font-size:12.5px;font-weight:700;color:var(--red);text-transform:uppercase}

/* contact */
.form-field{position:absolute;border:1.5px solid #bdbdbd;background:var(--white);font-size:13px;color:var(--field);padding:14px 13px}

/* footer */
.foot-nav{left:0;width:1200px;top:3485px;display:flex;justify-content:center;gap:27px}
.foot-nav a{color:var(--white);font-size:13px;font-weight:500;text-decoration:none;text-transform:uppercase}
.copyright{left:0;width:1200px;top:3523px;text-align:center;color:var(--white);font-size:12px}
.social{left:488px;top:3558px;display:flex;gap:20px}
.social span{width:18px;height:18px;border-radius:50%;background:var(--white)}
</style>
</head>
<body>

<svg class="shapes" viewBox="0 0 1200 3636" aria-hidden="true">
  <defs>
    <linearGradient id="heroGrad" x1="0" y1="0" x2="1" y2="1">
      <stop offset="0" stop-color="#3b4436"/><stop offset=".55" stop-color="#6c6a62"/><stop offset="1" stop-color="#3a4a2a"/>
    </linearGradient>
    <linearGradient id="darkGrad" x1="0" y1="0" x2="1" y2="0">
      <stop offset="0" stop-color="#1a1a1a"/><stop offset=".5" stop-color="#050505"/><stop offset="1" stop-color="#3a2a22"/>
    </linearGradient>
    <linearGradient id="dirtGrad" x1="0" y1="0" x2="1" y2="1">
      <stop offset="0" stop-color="#1e2a18"/><stop offset=".5" stop-color="#3a2a1e"/><stop offset="1" stop-color="#4a3424"/>
    </linearGradient>
  </defs>

  <!-- hero -->
  <g role="img" aria-label="Photo of a pitcher gripping a baseball in a packed stadium">
    <rect x="0" y="106" width="1200" height="700" fill="url(#heroGrad)"/>
  </g>
  <polygon points="0,775 1127,680 1127,697 0,805" fill="var(--red)"/>
  <polygon points="0,805 1127,697 1200,690 1200,806 0,806" fill="var(--white)"/>

  <!-- welcome -->
  <polygon points="89,840 340,840 89,862" fill="var(--red)"/>
  <g role="img" aria-label="Photo of a pitcher in a red uniform releasing a pitch">
    <defs><linearGradient id="wGrad" x1="0" y1="0" x2="0" y2="1"><stop offset="0" stop-color="#9fb4cc"/><stop offset=".6" stop-color="#b8453e"/><stop offset="1" stop-color="#7c8c55"/></linearGradient></defs>
    <polygon points="75,882 587,840 587,1207 75,1254" fill="url(#wGrad)"/>
  </g>

  <!-- sessions band -->
  <polygon points="73,1330 1200,1224 1200,1241 73,1347" fill="var(--red)"/>
  <g role="img" aria-label="Dark photo of a pitcher and a hand holding a baseball">
    <polygon points="0,1347 73,1347 1200,1241 1200,1842 0,1712" fill="url(#darkGrad)"/>
  </g>
  <polygon points="0,1708 1127,1817 1127,1832 0,1725" fill="var(--red)"/>

  <!-- gallery -->
  <g role="img" aria-label="Gallery photo of a pitcher in a stadium"><polygon points="0,1972 162,1982 162,2160 0,2170" fill="#4a5a6a"/></g>
  <g role="img" aria-label="Gallery photo of a pitcher in blue on a field"><polygon points="178,1969 402,1985 402,2155 178,2171" fill="#3f6e4a"/></g>
  <g role="img" aria-label="Gallery photo of a young pitcher mid-delivery"><rect x="418" y="1945" width="361" height="247" fill="#6d7a3c"/></g>
  <g role="img" aria-label="Gallery photo of a young pitcher striding forward"><polygon points="793,1983 1018,1969 1018,2171 793,2155" fill="#6f8aa4"/></g>
  <g role="img" aria-label="Gallery photo of a softball pitcher on a dirt mound"><polygon points="1033,1983 1200,1969 1200,2171 1033,2160" fill="#a8b48a"/></g>

  <!-- testimonials -->
  <polygon points="73,2379 1200,2273 1200,2290 73,2396" fill="var(--red)"/>
  <g role="img" aria-label="Photo of a baseball resting on infield dirt">
    <polygon points="0,2396 73,2396 1200,2290 1200,2894 0,2767" fill="url(#dirtGrad)"/>
  </g>
  <polygon points="0,2767 1127,2873 1127,2887 0,2784" fill="var(--red)"/>

  <!-- contact -->
  <polygon points="89,2934 340,2934 89,2956" fill="var(--red)"/>
  <g role="img" aria-label="Photo of a pitcher holding a baseball under stadium lights">
    <defs><linearGradient id="cGrad" x1="0" y1="0" x2="1" y2="1"><stop offset="0" stop-color="#2c3a2a"/><stop offset=".5" stop-color="#6a6862"/><stop offset="1" stop-color="#1d2a22"/></linearGradient></defs>
    <polygon points="75,2976 587,2934 587,3301 75,3349" fill="url(#cGrad)"/>
  </g>

  <!-- footer -->
  <polygon points="73,3424 1200,3320 1200,3338 73,3442" fill="var(--red)"/>
  <polygon points="0,3452 73,3442 1200,3338 1200,3636 0,3636" fill="var(--black)"/>
</svg>

<!-- header -->
<header>
  <div class="abs logo"><span class="logo-mark"></span><span class="logo-name">Dalworth Pitching Mechanics</span></div>
  <nav class="abs main-nav">
    <a href="#" class="active">Home</a><a href="#">About Us</a><a href="#">Services</a><a href="#">Sessions</a><a href="#">Latest News</a><a href="#">Testimonials</a><a href="#">Contact Us</a>
  </nav>
</header>

<!-- hero -->
<section class="hero">
  <h1 class="abs hero-title">Dalworth <span class="hl">Pitching</span><br>Mechanics</h1>
  <p class="abs hero-sub">We provide Private pitching sessions with a Division 1 PJTB baseball pitcher.</p>
  <a class="btn" href="#" style="left:75px;top:477px;width:178px;height:50px">Request Sessions</a>
  <div class="dots" style="left:75px;top:694px"><span class="on"></span><span></span><span></span><span></span></div>
</section>

<!-- welcome -->
<section class="welcome">
  <h2 class="abs section-title" style="left:617px;top:866px">Welcome to<br><span class="hl">Dalworth Pitching</span> Mechanics</h2>
  <p class="abs body-copy" style="left:617px;top:954px;width:500px">Sed ut perspiciatis unde omnis iste natus error sit voluptatem accusantium doloremque laudantium, totam rem aperiam, eaque ipsa quae ab illo inventore veritatis et quasi architecto beatae vitae dicta sunt explicabo. Nemo enim ipsam voluptatem quia voluptas sit aspernatur aut odit aut fugit, sed quia consequuntur magni dolores eos qui ratione voluptatem.</p>
  <a class="btn" href="#" style="left:617px;top:1124px;width:151px;height:48px">Read More</a>
</section>

<!-- sessions -->
<section class="sessions">
  <h2 class="abs sessions-title">Private pitching sessions with a <span class="hl">Division<br>1 PJTB baseball pitcher</span></h2>
  <p class="abs sessions-copy">Sed ut perspiciatis unde omnis iste natus error sit voluptatem accusantium doloremque laudantium, totam rem aperiam, eaque ipsa quae ab illo inventore veritatis et quasi architecto beatae vitae dicta sunt explicaboemo enim ipsam voluptatem quia voluptas sit aspernatur aut odit aut fugit, sed quia consequuntur magni dolores eos qui ratione voluptatem sunt in culpa qui officia deserunt mollit anim id est laborum.</p>
  <a class="btn" href="#" style="left:512px;top:1623px;width:176px;height:50px">Request Sessions</a>
</section>

<!-- gallery -->
<section class="gallery">
  <h2 class="abs section-title" style="left:0;width:1200px;top:1883px;text-align:center">Photo <span class="hl">Gallery</span></h2>
  <div class="dots grey" style="left:565px;top:2224px"><span class="on"></span><span></span><span></span><span></span></div>
</section>

<!-- testimonials -->
<section class="testimonials">
  <h2 class="abs section-title" style="left:75px;top:2438px;color:var(--white)">Testimonials</h2>
  <div class="testi-card" style="left:75px"><span class="quote">“</span><p>Sed ut perspiciatis unde omnis iste natus error sit voluptatem accusantium dolo emque laudantium, totam rem aperiam, eaque ipsa quae ab illo inventore enim ipsam voluptatem quia volup..”</p><div class="testi-name">-Name Heading</div></div>
  <div class="testi-card" style="left:436px"><span class="quote">“</span><p>Sed ut perspiciatis unde omnis iste natus error sit voluptatem accusantium dolo emque laudantium, totam rem aperiam, eaque ipsa quae ab illo inventore enim ipsam voluptatem quia volup..”</p><div class="testi-name">-Name Heading</div></div>
  <div class="testi-card" style="left:798px"><span class="quote">“</span><p>Sed ut perspiciatis unde omnis iste natus error sit voluptatem accusantium dolo emque laudantium, totam rem aperiam, eaque ipsa quae ab illo inventore enim ipsam voluptatem quia volup..”</p><div class="testi-name">-Name Heading</div></div>
  <div class="dots grey" style="left:565px;top:2742px"><span class="on"></span><span></span><span></span><span></span></div>
</section>

<!-- contact -->
<section class="contact">
  <h2 class="abs section-title" style="left:617px;top:2942px">Contact <span class="hl">Us</span></h2>
  <div class="form-field" style="left:615px;top:2997px;width:250px;height:48px">First Name</div>
  <div class="form-field" style="left:877px;top:2997px;width:250px;height:48px">Last Name</div>
  <div class="form-field" style="left:615px;top:3058px;width:250px;height:48px">Email Address</div>
  <div class="form-field" style="left:877px;top:3058px;width:250px;height:48px">Phone No</div>
  <div class="form-field" style="left:615px;top:3119px;width:512px;height:108px">Message</div>
  <a class="btn" href="#" style="left:617px;top:3241px;width:151px;height:48px">Submit</a>
</section>

<!-- footer -->
<footer>
  <nav class="abs foot-nav"><a href="#">Home</a><a href="#">About Us</a><a href="#">Services</a><a href="#">Sessions</a><a href="#">Latest News</a><a href="#">Testimonials</a><a href="#">Contact Us</a></nav>
  <p class="abs copyright">Copyright © 2023 Company Name All Rights Reserved</p>
  <div class="abs social">
    <span role="img" aria-label="Social link one"></span>
    <span role="img" aria-label="Social link two"></span>
    <span role="img" aria-label="Social link three"></span>
    <span role="img" aria-label="Social link four"></span>
    <span role="img" aria-label="Social link five"></span>
  </div>
</footer>

</body>
</html>
```